KTN Laredo Nuevo Artist Odette Pembrook event

Odette Pembrook

Elevate your appreciation for the arts with an Only-in-KTN VIP tour of the priceless art collection of El Paso's mysterious Odette, including access to her museum which is not open to the public. Dinner and transportation between sites included.

Odette Pembrook lives and works in El Paso, Texas. Praised by the Harbor Daily Courier as "fresh," "a tough act to follow," and the "ultimate in transgression," Pembrook is widely recognized in her home state of Texas as a unique presence and highly original artist. She has been characterized by Linda Fairweather, former curator at the Brightwater Gallery of Fine Works, as "an anachronism who earnestly pursues a long-held tradition of landscape and genre painting . . . inspired by her Southwestern environment and vivid imagination.

Rendered with thick applications of radiant colors, Pembrook's paintings are intensely personal, dream-like explorations of the natural world.
DATE: Wednesday, September 26, 2018
VENUE: RIO VISTA CIVIC TRUST HALL
518 W Calloway Ave
El Paso, TX 79947
United States
AGENDA: 6:00 - 7:30 Light supper and orientation to the mysterious Odette Pembrook, Rio Vista Civic Trust Hall downtown
7:30 - 7:45 Board van to go to Sagebrook Health Campus Odette Pembrook Chapel
7:45 - 8:15 View Chapel
8:15 - 8:30 Board van to go to Museum Pembrook
8:30 - 9:15 View Museum Pembrook with dessert
9:15 - 9:30 Return downtown
RESOURCE(S): Celia Wendt - Being an icon in the art world, and not needing any introduction, Celia probably knows more about Odette Pembrook than anyone!

Tomas Gable – President and CEO of the Rio Vista Civic Trust since 2011

Loranne Vega - Director of Presentations of the Odette Pembrook Museum and an art history graduate of SWCU

Neil Strauber - Nobody has ever actually seen Odette Pembrook, yet ophthalmologist and KTN member Dr. Neil Strauber is her eye surgeon. How can that be? Find out at the event!
ATTENDANCE: KTN Members, KTN Spouses/Guests, KTN SILVER Members, KTN SILVER Spouses/Guests
ATTIRE: Business Casual
DAY CHAIRS: Neil Strauber
Celia Wendt

Invite 5x7 or 7x5 please

Target Market(s)

KTN Laredo Nuevo Members

Industry/Entity Type

Non Profit

Font styles to use
Decorative
Script

Colors

Designer to choose colors to be used in the design.

Requirements
Must have
• Event title
• Date
• Artist description (Odette Pembrook)
• Venue
• Attire
• Attendees
• Logos
Nice to have
• Information about the artist
Should not have
• Art from another artists

```html
<!DOCTYPE html>
<html lang="en">
<head>
<meta charset="utf-8">
<title>Odette Pembrook – KTN Laredo Nuevo Invitation</title>
<link rel="stylesheet" href="https://fonts.googleapis.com/css2?family=Berkshire+Swash&family=Raleway:wght@400;500;700;800&display=swap">
<style>
  :root{
    --backdrop:#a8a8a8;
    --red-deep:#8e1712;
    --red:#b81f1b;
    --red-bright:#c8231f;
    --gold:#dcc08e;
    --gold-soft:#e6cfa3;
    --cream:#f4ead8;
    --white:#ffffff;
    --ink:#1d1d1d;
    --slate:#4a4f58;
    --navy:#27305a;
  }
  *{box-sizing:border-box;margin:0;padding:0}
  html,body{width:1200px;height:717px;overflow:hidden}
  body{background:var(--backdrop);font-family:"Raleway",sans-serif;position:relative}

  .card{position:absolute;top:0;height:717px;width:512px;overflow:hidden;box-shadow:0 0 8px rgba(0,0,0,.25)}
  .card--front{left:74px}
  .card--back{left:606px;background:var(--white)}

  .painting{position:absolute;inset:0}
  .painting--front{
    background:
      radial-gradient(ellipse at 30% 20%, rgba(220,70,50,.45), transparent 55%),
      radial-gradient(ellipse at 75% 65%, rgba(90,10,10,.45), transparent 60%),
      linear-gradient(160deg,#c2391f 0%,#a01e14 45%,#8a1710 75%,#a32316 100%);
  }
  .painting--back{
    bottom:auto;height:541px;
    background:
      radial-gradient(ellipse at 55% 72%, rgba(40,5,5,.55), transparent 45%),
      linear-gradient(180deg,var(--red-bright) 0%,var(--red) 50%,#a91a16 100%);
  }

  /* front */
  .bio{position:absolute;left:103px;top:80px;width:225px;color:var(--cream);font-size:9.6px;line-height:15.1px;text-align:justify;font-weight:400}
  .bio p{margin:0}
  .bio .dropcap{float:left;font-size:66px;line-height:50px;color:var(--gold);font-weight:400;margin:3px 5px 0 0}
  .title{position:absolute;left:0;width:100%;top:372px;text-align:center;font-family:"Berkshire Swash",cursive;color:var(--gold);line-height:60px}
  .title span{display:block}
  .title .first{font-size:62px;padding-left:10px}
  .title .last{font-size:66px;letter-spacing:-1px}
  .pitch{position:absolute;left:103px;top:526px;width:310px;color:var(--white);font-weight:700;font-size:13px;line-height:20px;text-align:justify;letter-spacing:.2px}
  .pitch strong{color:var(--gold);font-weight:800}

  /* back */
  .section-head{position:absolute;left:52px;font-family:"Berkshire Swash",cursive;color:var(--gold);font-size:19px}
  .resources-head{top:42px}
  .agenda-head{top:226px}
  .cols{position:absolute;left:52px;width:410px;display:grid;grid-template-columns:1fr 1fr;column-gap:22px;color:var(--white)}
  .resources{top:72px;font-size:9.6px;line-height:15.2px}
  .resources .entry{margin-bottom:15px}
  .resources b{font-weight:700}
  .agenda{top:258px;font-size:11.6px;line-height:15px;grid-template-columns:214px 1fr}
  .agenda .item{margin-bottom:15px}
  .agenda b{font-weight:700}
  .rule{position:absolute;left:52px;width:410px;height:1px;background:var(--gold)}
  .rule--one{top:218px}
  .rule--two{top:418px}
  .details{position:absolute;left:52px;top:453px;color:var(--white);font-size:8.4px;line-height:17px}
  .details b{font-weight:800}

  .brands{position:absolute;top:556px;left:0;width:100%;display:flex;justify-content:center;align-items:center;gap:26px}
  .brand{display:flex;align-items:center;gap:7px;font-weight:700;font-size:20px;letter-spacing:1px}
  .brand--event{color:var(--slate)}
  .brand--chapter{color:var(--navy);font-size:16px;letter-spacing:.5px}
  .mark{display:inline-block;width:14px;height:14px;background:currentColor}
  .mark--round{border-radius:50%}

  .event-info{position:absolute;top:645px;left:0;width:100%;text-align:center;color:var(--ink);font-size:10.6px;line-height:13.6px}
  .event-info b{font-weight:700}
  .footer-bar{position:absolute;left:132px;bottom:0;width:248px;height:8px;background:var(--red)}
</style>
</head>
<body>

<section class="card card--front">
  <div class="painting painting--front" role="img" aria-label="Abstract red painted texture of swirling brushstrokes"></div>

  <div class="bio">
    <p><span class="dropcap">A</span>Odette Pembrook lives and works in El Paso, Texas. Praised by the Harbor Daily Courier as “fresh,” “a tough act to follow,” and the “ultimate in transgression,” Pembrook is widely recognized in her home state of Texas as a unique presence and highly original artist.</p>
    <p>She has been characterized by Linda Fairweather, former curator at the Brightwater Gallery of Fine Works, as “an anachronism who earnestly pursues a long-held tradition of landscape and genre painting . . . inspired by her Southwestern environment and vivid imagination.</p>
    <p>Rendered with thick applications of radiant colors, Pembrook’s paintings are intensely personal, dream-like explorations of the natural world.</p>
  </div>

  <h1 class="title"><span class="first">Odette</span><span class="last">Pembrook</span></h1>

  <p class="pitch">Elevate your appreciation for the arts with an Only-in-KTN VIP tour of the <strong>PRICELESS ART COLLECTION</strong> of <strong>EL PASO’S MYSTERIOUS ODETTE</strong>, including access to her museum which is not open to the public. Dinner and transportation between sites included.</p>
</section>

<section class="card card--back">
  <div class="painting painting--back" role="img" aria-label="Red painted texture with a dark brushstroke swirl"></div>

  <h2 class="section-head resources-head">Resource(s):</h2>
  <div class="cols resources">
    <div>
      <p class="entry"><b>Celia Wendt</b> – Being an icon in the art world, and not needing any introduction, Celia probably knows more about Odette Pembrook than anyone!</p>
      <p class="entry"><b>Tomas Gable</b> – President and CEO of the Rio Vista Civic Trust since 2011</p>
    </div>
    <div>
      <p class="entry"><b>Loranne Vega</b> – Director of Presentations of the Odette Pembrook Museum and an art history graduate of SWCU</p>
      <p class="entry"><b>Neil Strauber</b> – Nobody has ever actually seen Odette Pembrook, yet ophthalmologist and KTN member Dr. Neil Strauber is her eye surgeon. How can that be? Find out at the event!</p>
    </div>
  </div>
  <div class="rule rule--one"></div>

  <h2 class="section-head agenda-head">Agenda:</h2>
  <div class="cols agenda">
    <div>
      <p class="item"><b>6:00 - 7:30</b> Light supper and orientation to the mysterious Odette Pembrook, Rio Vista Civic Trust Hall downtown</p>
      <p class="item"><b>7:30 - 7:45</b> Board van to go to Sagebrook Health Campus Odette Pembrook Chapel</p>
    </div>
    <div>
      <p class="item"><b>7:45 - 8:15</b> View Chapel</p>
      <p class="item"><b>8:15 - 8:30</b> Board van to go to Museum Pembrook</p>
      <p class="item"><b>8:30 - 9:15</b> View Museum Pembrook with dessert</p>
      <p class="item"><b>9:15 - 9:30</b> Return downtown</p>
    </div>
  </div>
  <div class="rule rule--two"></div>

  <div class="details">
    <p><b>ATTENDEES: KTN Member/Spouse, KTN SILVER Member/Spouse</b></p>
    <p><b>ATTIRE:</b> Business Casual</p>
    <p><b>DAY CHAIRS:</b> Neil Strauber, Celia Wendt</p>
  </div>

  <div class="brands">
    <div class="brand brand--event"><span class="mark mark--round"></span>ASCEND 947</div>
    <div class="brand brand--chapter"><span class="mark"></span>KTN Laredo Nuevo</div>
  </div>

  <div class="event-info">
    <p><b>DATE:</b> Wednesday, September 26, 2018</p>
    <p><b>VENUE:</b> RIO VISTA CIVIC TRUST HALL</p>
    <p>518 W Calloway Ave, El Paso, TX 79947</p>
    <p>United States</p>
  </div>
  <div class="footer-bar"></div>
</section>

</body>
</html>
```